Emberdance 2018

Design an invitation and accompanying envelope for a charity event. Invitation would need front and back designed with information on the inside. Should match the design for the save the date.

```html
<!DOCTYPE html>
<html lang="en">
<head>
<meta charset="utf-8">
<title>Ember Dance Invitation</title>
<link rel="stylesheet" href="https://fonts.googleapis.com/css2?family=Cormorant+Garamond:wght@300;400&family=Cormorant+SC:wght@400;500&family=Montserrat:wght@300;400;600&display=swap">
<style>
  :root {
    --page-bg: #e4e4e4;
    --night: #0f1020;
    --night-deep: #080914;
    --paper: #ffffff;
    --ghost: #ebebeb;
    --ink: #2a2a2a;
    --rose: #c9343d;
    --teal: #2b7fa8;
    --coral: #d85b4e;
    --violet: #7b6fc2;
    --brand-blue: #1f63b0;
    --muted-white: #c9c9d4;
  }
  * { box-sizing: border-box; margin: 0; padding: 0; }
  html, body { width: 798px; height: 1200px; overflow: hidden; }
  body {
    background: var(--page-bg);
    font-family: "Montserrat", sans-serif;
    position: relative;
  }
  .card {
    position: absolute;
    left: 58px;
    width: 680px;
    height: 526px;
    overflow: hidden;
  }
  .card--outside {
    top: 40px;
    background: radial-gradient(ellipse at 60% 45%, #16182e 0%, var(--night) 55%, var(--night-deep) 100%);
  }
  .card--inside { top: 615px; background: var(--paper); }
  .fold {
    position: absolute; left: 340px; top: 0; width: 1px; height: 100%;
  }
  .card--outside .fold { background: rgba(255,255,255,0.04); }
  .card--inside .fold { background: rgba(0,0,0,0.05); }

  .art-area { position: absolute; left: 0; top: 0; }

  .spine-title {
    position: absolute;
    left: 62px; top: 232px;
    transform: translate(-50%, -50%) rotate(-90deg);
    font-family: "Cormorant Garamond", serif;
    font-weight: 300;
    font-size: 88px;
    line-height: 1;
    color: rgba(255,255,255,0.06);
    white-space: nowrap;
  }

  .event-title {
    position: absolute;
    font-family: "Cormorant Garamond", serif;
    font-weight: 300;
    line-height: 0.9;
    white-space: nowrap;
    background: linear-gradient(100deg, #4a6cf0 0%, #b566d8 40%, #e26b4a 70%, #c7395f 100%);
    -webkit-background-clip: text;
    background-clip: text;
    color: transparent;
  }
  .event-title span { display: block; }
  .event-title .second { padding-left: 0.8em; }
  .cover-title { left: 400px; top: 180px; font-size: 68px; }

  .brand {
    position: absolute; left: 448px; top: 436px;
  }
  .brand-name {
    display: flex; align-items: center; gap: 6px;
    font-family: "Montserrat", sans-serif;
    font-weight: 600;
    font-size: 24px;
    letter-spacing: 1px;
    color: var(--brand-blue);
  }
  .brand-name::before {
    content: ""; width: 9px; height: 9px; border-radius: 50%;
    background: var(--brand-blue);
  }
  .brand-tag {
    margin-top: 3px;
    font-size: 8px; font-weight: 600; color: #ffffff;
  }
  .brand-url {
    position: absolute; left: 448px; top: 500px; width: 130px;
    text-align: center;
    font-family: "Cormorant Garamond", serif;
    font-size: 8px; letter-spacing: 2px;
    color: var(--muted-white);
  }

  .ghost-title {
    position: absolute; left: 80px; top: 168px;
    font-family: "Cormorant Garamond", serif;
    font-weight: 300; font-size: 64px; line-height: 0.9;
    color: var(--ghost);
    white-space: nowrap;
  }
  .ghost-title span { display: block; }
  .ghost-title .second { padding-left: 0.8em; }

  .details {
    position: absolute; left: 0; width: 340px; top: 364px;
    text-align: center;
  }
  .details .edition {
    font-family: "Cormorant SC", serif; font-size: 17px; color: var(--coral);
    letter-spacing: 0.5px;
  }
  .details .date {
    margin-top: 8px;
    font-family: "Cormorant SC", serif; font-size: 24px; color: var(--teal);
    line-height: 1.1; letter-spacing: 0.5px;
  }
  .details .time {
    font-family: "Cormorant SC", serif; font-size: 24px; color: var(--coral);
    line-height: 1.1;
  }
  .details .venue {
    margin-top: 14px;
    font-family: "Cormorant SC", serif; font-size: 13px; color: var(--ink);
    line-height: 1.1;
  }

  .panel-right { position: absolute; left: 370px; width: 286px; text-align: center; }
  .section-heading {
    font-family: "Montserrat", sans-serif; font-weight: 300;
    font-size: 17px;
  }
  .section-body {
    font-size: 9.2px; line-height: 14.6px; color: var(--ink); font-weight: 400;
  }
  .invite { top: 56px; }
  .invite .section-heading { color: var(--rose); margin-bottom: 2px; }
  .mission { top: 380px; }
  .mission .section-heading { color: var(--violet); margin-bottom: 2px; }

  .title-frame {
    position: absolute; left: 431px; top: 214px; width: 148px; height: 128px;
    border-top: 1px solid var(--violet); border-bottom: 1px solid var(--violet);
  }
  .title-frame::before, .title-frame::after {
    content: ""; position: absolute; top: 0; width: 1px; height: 8px; background: var(--violet);
  }
  .title-frame::before { left: 0; }
  .title-frame::after { right: 0; }
  .tick-bottom-l, .tick-bottom-r {
    position: absolute; bottom: 0; width: 1px; height: 8px; background: var(--violet);
  }
  .tick-bottom-l { left: 0; }
  .tick-bottom-r { right: 0; }
  .inside-title { left: 420px; top: 236px; font-size: 50px; }
</style>
</head>
<body>
  <section class="card card--outside" aria-label="Invitation outside">
    <div class="fold"></div>
    <svg class="art-area" width="680" height="526" viewBox="0 0 680 526" role="img" aria-label="Space for a watercolour floral wreath illustration in rainbow tones">
      <defs>
        <radialGradient id="artGlow" cx="0.55" cy="0.5" r="0.55">
          <stop offset="0" stop-color="#9a4fc9" stop-opacity="0.32"/>
          <stop offset="0.6" stop-color="#c2477d" stop-opacity="0.12"/>
          <stop offset="1" stop-color="#0f1020" stop-opacity="0"/>
        </radialGradient>
      </defs>
      <rect x="120" y="0" width="560" height="526" fill="url(#artGlow)"/>
    </svg>
    <div class="spine-title">Emberdance</div>
    <div class="event-title cover-title"><span>Ember</span><span class="second">Dance</span></div>
    <div class="brand">
      <div class="brand-name">RIVORA</div>
      <div class="brand-tag">Lena Hart Memorial Foundation</div>
    </div>
    <div class="brand-url">WWW.RIVORAFUND.ORG</div>
  </section>

  <section class="card card--inside" aria-label="Invitation inside">
    <div class="fold"></div>
    <svg class="art-area" width="340" height="526" viewBox="0 0 340 526" role="img" aria-label="Space for a faint pale grey floral wreath ornament">
      <defs>
        <radialGradient id="ghostGlow" cx="0.5" cy="0.5" r="0.5">
          <stop offset="0" stop-color="#f3f3f3"/>
          <stop offset="1" stop-color="#ffffff" stop-opacity="0"/>
        </radialGradient>
      </defs>
      <rect x="20" y="80" width="320" height="280" fill="url(#ghostGlow)"/>
    </svg>
    <div class="ghost-title"><span>Ember</span><span class="second">Dance</span></div>
    <div class="details">
      <p class="edition">2ND ANNUAL EVENT</p>
      <p class="date">November 3, 2018</p>
      <p class="time">7PM</p>
      <p class="venue">The Linden Hall 240 Harbor St.<br>Brookfield, PA 15300</p>
    </div>

    <div class="panel-right invite">
      <h2 class="section-heading">You are cordially invited</h2>
      <p class="section-body">to spend an enchanting evening of dinner dancing and entertainment at The Linden Hall in the heart of the cultural district in Brookfield. We are celebrating the incredible work RIVORA has been able to accomplish with the help of incredible donors. We would love to share stories of how we are all changing lives and of course has an incredible time on the dance floor. Don't miss this yearly event.</p>
    </div>

    <div class="title-frame"><span class="tick-bottom-l"></span><span class="tick-bottom-r"></span></div>
    <div class="event-title inside-title"><span>Ember</span><span class="second">Dance</span></div>

    <div class="panel-right mission">
      <h2 class="section-heading">RIVORA's mission</h2>
      <p class="section-body">is to provide safe drinking water to fight against PREVENTABLE deaths by stopping the spread of waterborne diseases. Proceeds from the RIVORA Emberdance will go directly to funding clean water projects around the world and all ticket sales and sponsorships are tax deductible.</p>
    </div>
  </section>
</body>
</html>
```